Business card design for IT consulting company

Looking for a simple, modern, clean business card design.
Open to reworking our existing logo.

Attached is our current business cards which we do not like.
Ideally double sided with something simple on the back.
Rectangle / Horizonal only.
No rounded edges on the card.
White as the dominate color is preferred.

Target Market(s)

clients, legal, oil & gas, medical, professionals

Industry/Entity Type

IT, tech, consulting

Contact Information for Business Card

Name, Title, email, phone, cell, website

Font styles to use
Sans Serif

Requirements
Must have
• Clean design
Should not have
• loud colors or unusual fonts, etc

```html
<!DOCTYPE html>
<html lang="en">
<head>
<meta charset="utf-8">
<title>Orvel Solutions – Business Card</title>
<link rel="stylesheet" href="https://fonts.googleapis.com/css2?family=Open+Sans:wght@300;400;700&display=swap">
<style>
  :root {
    --bg: #dcdcdc;
    --card: #ffffff;
    --ink: #1a1a1a;
    --muted: #555555;
    --rule: #444444;
    --accent-blue: #48b0e3;
    --accent-navy: #29266e;
    --navy-soft: #35328a;
  }
  * { box-sizing: border-box; margin: 0; padding: 0; }
  html, body {
    width: 1200px; height: 1200px; overflow: hidden;
    background: var(--bg);
    font-family: "Open Sans", Arial, sans-serif;
  }
  .sheet {
    width: 1200px; height: 1200px;
    display: flex; flex-direction: column; align-items: center; justify-content: center;
    gap: 60px;
  }
  .card {
    position: relative;
    width: 900px; height: 514px;
    background: var(--card);
    box-shadow: 0 3px 5px rgba(0,0,0,0.35);
    overflow: hidden;
  }
  /* Front */
  .brand {
    position: absolute; left: 108px; top: 226px;
    display: flex; align-items: center; gap: 14px;
  }
  .brand-square { width: 58px; height: 58px; background: var(--accent-navy); }
  .brand-name { font-size: 31px; font-weight: 700; color: var(--ink); letter-spacing: -0.5px; white-space: nowrap; }
  .divider {
    position: absolute; left: 448px; top: 154px;
    width: 2px; height: 212px; background: var(--rule);
  }
  .person { position: absolute; left: 484px; top: 152px; }
  .person-name { font-size: 35px; font-weight: 700; color: var(--ink); line-height: 1.1; letter-spacing: -0.5px; white-space: nowrap; }
  .person-title { font-size: 22px; font-weight: 400; color: var(--accent-blue); margin-top: 4px; }
  .contact-list { list-style: none; margin-top: 36px; }
  .contact-list li {
    display: flex; align-items: center; gap: 10px;
    font-size: 19px; color: var(--muted); line-height: 29px;
  }
  .contact-list svg { width: 17px; height: 17px; flex: none; }
  /* Back */
  .card-back { background: var(--accent-navy); }
  .back-field {
    position: absolute; inset: 0;
    background: linear-gradient(135deg, var(--navy-soft) 0%, var(--accent-navy) 70%);
  }
  .back-name {
    position: absolute; left: 450px; top: 257px; width: 450px; height: 257px;
    display: flex; align-items: center; justify-content: center;
    color: #ffffff; font-size: 40px; font-weight: 700; letter-spacing: -0.5px;
    padding-top: 20px; white-space: nowrap;
  }
</style>
</head>
<body>
<main class="sheet">
  <section class="card card-front">
    <div class="brand">
      <span class="brand-square"></span>
      <span class="brand-name">Orvel Solutions</span>
    </div>
    <span class="divider"></span>
    <div class="person">
      <div class="person-name">Daniel Moreau</div>
      <div class="person-title">IT Consultant</div>
      <ul class="contact-list">
        <li>
          <svg viewBox="0 0 16 16"><path d="M4 2c1 0 2 3 1.5 3.8L4.6 6.7c.8 1.8 2.5 3.6 4.5 4.6l.9-.9c.8-.5 3.8.5 3.8 1.5 0 1.2-1.2 2.1-2.5 2.1C6.5 14 2 9.5 2 4.5 2 3.2 2.8 2 4 2z" fill="var(--accent-blue)"/></svg>
          (555) 014-2290
        </li>
        <li>
          <svg viewBox="0 0 16 16"><rect x="4" y="1.5" width="8" height="13" rx="1.2" fill="none" stroke="var(--accent-blue)" stroke-width="1.5"/><circle cx="8" cy="12.3" r="0.8" fill="var(--accent-blue)"/></svg>
          (555) 017-3481
        </li>
        <li>
          <svg viewBox="0 0 16 16"><rect x="1.5" y="3.5" width="13" height="9" fill="var(--accent-blue)"/><path d="M1.5 3.5 8 9l6.5-5.5" fill="none" stroke="#fff" stroke-width="1.2"/></svg>
          d.moreau@orvel.ca
        </li>
        <li>
          <svg viewBox="0 0 16 16" fill="none" stroke="var(--accent-blue)" stroke-width="1.2"><circle cx="8" cy="8" r="6.3"/><ellipse cx="8" cy="8" rx="2.8" ry="6.3"/><path d="M1.7 8h12.6M2.7 5h10.6M2.7 11h10.6"/></svg>
          www.orvel.ca
        </li>
      </ul>
    </div>
  </section>

  <section class="card card-back">
    <div class="back-field" role="img" aria-label="Brand colour field on the card back"></div>
    <span class="back-name">Orvel Solutions</span>
  </section>
</main>
</body>
</html>
```